webdesign for a spectacles/glasses designer

Hello,

Someone in my village designs his own spectacles/eyeglasses.

For this I need a design that looks better than my poor design skills ;o)

The site is based around collections, subcollections and the actual items.

So we need a design that lists these in a nice way, worst case on seperate pages.

Here you can find the working material...

https://www.filevault-example.com/s/q8rtk2mzp4vn71c/ArtHive.zip

keep an eye on the product_tree file.

first level is the collection name
2nd is the model group
3rd is the model (on most of them it's just a different color of the same base model)

I added a seperate contact info file (line is too slow to reupload 60Mb again :( )

https://dl.filevault-example.com/u/31946082/Marten/contact.zip

I think I forgot to mention that it will be a shop like site to present his products,
altho I will add a cart system there won't be a payment system linked to it as
people who place orders will get contacted with payment instructions.
Updates

In the zipfile /Logo/logo_mistral_font.psd is the main logo
(you need to change character spacing to 1 to get rid of the spacing gaps)

the other one is only a collection logo

Target Market(s)

Plain customers and his resellers.

Industry/Entity Type

Shop

Requirements
Must have
• - a design that suits responsive behaviour (via the 960 grid)
- a menu is always handy (home, about, collections, contact)
- highlighted area/slider to highlight his sunglasses over glasses thingy
- featured products (newly added or promotional stuff)

there is a lot of pretty pictures to be supplied so do what you think is best

Nice to have
• a roll over zoom with selectable thumbnails or a plain gallery with full picture display at the product page.

maybe a drop down menu for the collection part (I will supply a screenshot of the backend structure)

```html
<!DOCTYPE html>
<html lang="en">
<head>
<meta charset="utf-8">
<title>Marten – Eyewear</title>
<link href="https://fonts.googleapis.com/css2?family=Cabin:wght@400;500;600&display=swap" rel="stylesheet">
<style>
  :root{
    --orange:#ff5a0e;
    --orange-soft:#f26a3c;
    --ink:#1a1a1a;
    --muted:#555;
    --line:#dcdcdc;
    --rule:#e1e4e3;
    --footer:#343434;
    --footer-base:#282828;
    --white:#fff;
  }
  *{margin:0;padding:0;box-sizing:border-box}
  html,body{width:1007px;height:1200px;overflow:hidden;background:var(--white)}
  body{position:relative;font-family:"Cabin",Arial,sans-serif;color:var(--ink)}
  .abs{position:absolute}

  /* header */
  .brand{left:102px;top:24px;font-size:40px;font-weight:600;color:var(--ink);letter-spacing:.5px}
  .cart{left:826px;top:61px;display:flex;align-items:center;gap:6px;font-family:Arial,sans-serif;font-size:11px}
  .cart .label{color:var(--orange-soft)}
  .header-rule{left:0;top:108px;width:1007px;height:2px;background:#e6e6e6}

  /* nav */
  .nav{left:0;top:110px;width:1007px;height:47px}
  .nav a{position:absolute;top:15px;font-size:15px;color:var(--ink);text-decoration:none}
  .nav a.active{color:var(--orange-soft)}
  .search{left:732px;top:119px;width:181px;height:30px;border:1px solid #d5d5d5;border-radius:15px;display:flex;align-items:center;padding-left:10px;gap:6px;font-size:10.5px;color:#8a8f99}
  .nav-rule{left:0;top:157px;width:1007px;height:4px;background:#e3e3e3}

  /* hero */
  .hero{left:0;top:161px;width:1007px;height:415px;background:radial-gradient(ellipse at 55% 55%,#c99a78 0%,#a07a5e 28%,#6e6a66 55%,#5d5d5d 100%)}
  .hero-rule{left:0;top:576px;width:1007px;height:3px;background:var(--orange-soft)}
  .hero-arrow{top:331px}

  /* featured */
  .section-title{left:0;top:616px;width:1007px;text-align:center;font-size:20px;font-weight:400;letter-spacing:.2px}
  .section-rule{left:92px;top:657px;width:823px;height:3px;background:var(--rule)}
  .section-notch{left:500px;top:655px}

  .card-highlight{left:91px;top:696px;width:189px;height:321px;border:3px solid var(--orange);border-radius:10px}
  .divider{top:709px;width:1px;height:289px;background:#e8e8e8}

  .product{top:727px;width:210px;text-align:center}
  .product .thumb{width:151px;height:122px;margin:0 auto}
  .thumb.portrait{background:linear-gradient(160deg,#7b7470,#b48a6c 50%,#4f4c4a)}
  .thumb.purple{background:linear-gradient(135deg,#f4f2f6,#e7e2ec 60%,#b28fbf)}
  .thumb.orange{background:linear-gradient(135deg,#f3f3f3 20%,#e64a1c 45%,#f39a1a 75%,#e23a18)}
  .product h3{margin-top:23px;font-size:19px;font-weight:400;line-height:1.2}
  .product .desc{margin-top:6px;font-size:10.5px;line-height:15px;color:var(--muted);letter-spacing:.2px}
  .product .price{margin-top:10px;font-family:Arial,sans-serif;font-weight:700}
  .price .was{font-size:9px;color:var(--orange-soft);text-decoration:line-through;font-weight:400;margin-right:3px}
  .price .now{font-size:14.5px;color:#8a2a20}
  .btn{display:inline-block;margin-top:6px;width:106px;height:28px;line-height:28px;border-radius:14px;background:var(--orange);color:var(--white);font-family:Arial,sans-serif;font-size:11px;font-weight:700}

  /* footer */
  .footer{left:0;top:1055px;width:1007px;height:118px;background:var(--footer);color:var(--white)}
  .footer h4{position:absolute;top:27px;font-size:15px;font-weight:400}
  .footer ul{position:absolute;top:57px;list-style:none;font-family:Arial,sans-serif;font-size:11px;line-height:15px}
  .footer li::before{content:"";display:inline-block;border-left:4px solid var(--white);border-top:3px solid transparent;border-bottom:3px solid transparent;margin:0 8px 1px 2px}
  .newsletter{position:absolute;left:709px;top:58px;width:180px;height:26px;background:var(--white);display:flex;border:2px solid var(--white)}
  .newsletter span{flex:1;font-family:Arial,sans-serif;font-size:11px;color:#999;line-height:22px;padding-left:5px}
  .newsletter b{width:52px;background:#3a3a3a;color:var(--white);font-family:Arial,sans-serif;font-weight:400;font-size:11px;text-align:center;line-height:22px}
  .copyright{left:0;top:1173px;width:1007px;height:27px;background:var(--footer-base);color:#ddd;text-align:center;font-family:Arial,sans-serif;font-size:10.5px;line-height:27px}
</style>
</head>
<body>

<header>
  <div class="abs brand">Marten</div>
  <div class="abs cart">
    <svg width="26" height="24" viewBox="0 0 26 24" aria-hidden="true">
      <path d="M1 3h4l3 12h13l3-9H7" fill="none" stroke="#e0652e" stroke-width="2"/>
      <path d="M9 8h13M10 11h11" stroke="#e0652e" stroke-width="1.5"/>
      <circle cx="10" cy="20" r="2" fill="#555"/><circle cx="19" cy="20" r="2" fill="#555"/>
    </svg>
    <span>25 <span class="label">Itmes</span></span>
  </div>
  <div class="abs header-rule"></div>
</header>

<nav class="abs nav">
  <a class="active" style="left:102px">Home</a>
  <a style="left:195px">About</a>
  <a style="left:300px">Collections</a>
  <a style="left:430px">Contact</a>
</nav>
<div class="abs search">
  <svg width="14" height="14" viewBox="0 0 14 14" aria-hidden="true"><circle cx="6" cy="6" r="4.5" fill="none" stroke="#b5b5b5" stroke-width="1.5"/><path d="M9.5 9.5L13 13" stroke="#b5b5b5" stroke-width="1.5"/></svg>
  Type and hit enter
</div>
<div class="abs nav-rule"></div>

<section>
  <div class="abs hero" role="img" aria-label="Slider photo: woman wearing orange-framed glasses with a tinted sun overlay flipped up"></div>
  <svg class="abs hero-arrow" style="left:52px" width="46" height="94" viewBox="0 0 46 94" aria-hidden="true"><path d="M40 2L6 47l34 45" fill="none" stroke="rgba(255,255,255,.45)" stroke-width="9"/></svg>
  <svg class="abs hero-arrow" style="left:906px" width="46" height="94" viewBox="0 0 46 94" aria-hidden="true"><path d="M6 2l34 45L6 92" fill="none" stroke="rgba(255,255,255,.45)" stroke-width="9"/></svg>
  <div class="abs hero-rule"></div>
</section>

<section>
  <h2 class="abs section-title">FEATURED PRODUCTS</h2>
  <div class="abs section-rule"></div>
  <svg class="abs section-notch" width="16" height="10" viewBox="0 0 16 10" aria-hidden="true"><path d="M0 2h3l5 6 5-6h3" fill="#fff" stroke="#e1e4e3" stroke-width="2"/></svg>

  <div class="abs card-highlight"></div>
  <div class="abs divider" style="left:311px"></div>
  <div class="abs divider" style="left:523px"></div>
  <div class="abs divider" style="left:738px"></div>

  <article class="abs product" style="left:80px">
    <div class="thumb portrait" role="img" aria-label="Woman wearing sunglasses overlay, red frame"></div>
    <h3>ROV 02</h3>
    <p class="desc">Stylish Overlay Sunglasses<br>Red Frame</p>
    <p class="price"><span class="was">$89</span><span class="now">$69</span></p>
    <span class="btn">ADD TO CART</span>
  </article>

  <article class="abs product" style="left:319px">
    <div class="thumb purple" role="img" aria-label="Close-up of purple glasses frame"></div>
    <h3>MC25- Col03</h3>
    <p class="desc">Classy Glasses<br>Purple/Red&nbsp; Framed</p>
    <p class="price"><span class="was">$89</span><span class="now">$69</span></p>
    <span class="btn">ADD TO CART</span>
  </article>

  <article class="abs product" style="left:528px">
    <div class="thumb portrait" role="img" aria-label="Woman wearing sunglasses overlay, black frames"></div>
    <h3>ROV 02</h3>
    <p class="desc">Stylish Overlay Sunglasses<br>Black Frames</p>
    <p class="price"><span class="was">$89</span><span class="now">$69</span></p>
    <span class="btn">ADD TO CART</span>
  </article>

  <article class="abs product" style="left:737px">
    <div class="thumb orange" role="img" aria-label="Close-up of orange and red glasses temple"></div>
    <h3>MC22- Col03 02</h3>
    <p class="desc">Extra Countoured glasses<br>Orange/Red Framed</p>
    <p class="price"><span class="was">$89</span><span class="now">$69</span></p>
    <span class="btn">ADD TO CART</span>
  </article>
</section>

<footer>
  <div class="abs footer">
    <h4 style="left:111px">BEST SELLERS</h4>
    <ul style="left:111px"><li>Women</li><li>Men</li></ul>
    <h4 style="left:277px">Eye Glasses</h4>
    <ul style="left:276px"><li>Women</li><li>Men</li></ul>
    <h4 style="left:435px">Sun Glasses</h4>
    <ul style="left:432px"><li>Women</li><li>Men</li></ul>
    <h4 style="left:709px">Subscribe Newsletter</h4>
    <div class="newsletter"><span>Enter your email</span><b>Submit</b></div>
  </div>
  <div class="abs copyright">Marten @ copyright 2013 | 2013 - 2014 Privacy Policy</div>
</footer>

</body>
</html>
```